Winery needs to update tired, conservative wine label

We are a winery based in the Clare Valley of South Australia. We are looking to give an old, tired wine label a modern update to use particularly on Rose, but also across other vatieties including Riesling, Shiraz and Cabernet. The label could utilise parts of the old logo (horse shoe, grapes, leaves) but in a fresh modern way. Old artwork has been uploaded to show label as it currently is. We are looking for a label that pays tribute to the history of the brand (Colin Fennick: established 1977) but gives it a fresh, clean appearance that will be attractive to young professionals.

Target Market(s)

Male and Female young professionals, particularly Rose drinkers.

Font styles to use
Serif
Sans Serif

Colors

Designer to choose colors to be used in the design.

Requirements
Must have
• It must use the name Colin Fennick on the label, show region, vintage and variety. The label must work on a number of different wine bottle shapes and glass colours

```html
<!DOCTYPE html>
<html lang="en">
<head>
<meta charset="utf-8">
<title>Colin Fennick – Label Range</title>
<link rel="stylesheet" href="https://fonts.googleapis.com/css2?family=Bebas+Neue&family=Oswald:wght@500;600&family=Roboto+Condensed:wght@400&display=swap">
<style>
  :root {
    --bg-centre: #ffffff;
    --bg-edge: #e9e9e9;
    --ink: #231f20;
    --ink-soft: #161616;
    --paper: #f7f7f5;
    --slate: #2c2d2f;
    --gold: #c49a2c;
    --white: #ffffff;
    --grey-text: #6b6b6b;
  }
  * { margin: 0; padding: 0; box-sizing: border-box; }
  html, body { width: 1200px; height: 1000px; overflow: hidden; }
  body {
    position: relative;
    background: radial-gradient(ellipse at 50% 40%, var(--bg-centre) 0%, var(--bg-centre) 45%, var(--bg-edge) 100%);
    font-family: "Roboto Condensed", Arial, sans-serif;
  }

  /* Flat front labels */
  .label {
    position: absolute;
    top: 470px;
    width: 200px;
    height: 210px;
    display: flex;
    flex-direction: column;
    justify-content: center;
    padding-left: 34px;
  }
  .label--white { left: 196px; background: var(--paper); box-shadow: 0 0 0 1px #e2e2e2; }
  .label--slate { left: 515px; background: var(--slate); }
  .label--slate-bright { left: 826px; background: var(--slate); }

  .label--white .wordmark__name,
  .label--white .wordmark__meta { color: var(--ink); }
  .label--slate .wordmark__name { color: var(--ink-soft); }
  .label--slate .wordmark__meta { color: #1d1d1d; }
  .label--slate-bright .wordmark__name,
  .label--slate-bright .wordmark__meta { color: var(--white); }

  /* Wordmark block shared by labels and range lockups */
  .wordmark { display: inline-block; }
  .wordmark__head { display: flex; align-items: flex-start; gap: 6px; }
  .wordmark__name {
    font-family: "Bebas Neue", "Oswald", sans-serif;
    font-weight: 400;
    font-size: 50px;
    line-height: 0.86;
    color: var(--ink);
    white-space: nowrap;
  }
  .wordmark__dot {
    width: 14px; height: 14px;
    border-radius: 50%;
    background: var(--gold);
    margin-top: 4px;
    flex: none;
  }
  .wordmark__meta {
    font-size: 9.5px;
    letter-spacing: 0.3px;
    color: var(--ink);
    margin-top: 4px;
    white-space: nowrap;
  }
  .wordmark__variety {
    font-family: "Oswald", sans-serif;
    font-weight: 600;
    font-size: 19px;
    line-height: 1.05;
    color: var(--gold);
    white-space: nowrap;
    margin-top: 1px;
  }
  .wordmark__vintage {
    font-size: 7px;
    letter-spacing: 0.6px;
    color: var(--gold);
    text-align: right;
    white-space: nowrap;
  }

  /* Range lockups */
  .range { position: absolute; top: 788px; }
  .range--shiraz { left: 180px; }
  .range--shiraz-cab { left: 410px; }
  .range--riesling { left: 640px; }
  .range--cab-sav { left: 870px; }

  .range .wordmark__name { font-size: 66px; }
  .range .wordmark__dot { width: 18px; height: 18px; margin-top: 6px; }
  .range .wordmark__meta { font-size: 11.5px; margin-top: 6px; }
  .range .wordmark__variety { font-size: 20px; }
  .range .wordmark__vintage { font-size: 8px; }

  .variety-row { display: flex; align-items: flex-start; gap: 6px; }
  .variety-row .wordmark__vintage { text-align: left; line-height: 1.05; margin-top: 3px; }
</style>
</head>
<body>

  <!-- Front labels -->
  <section class="label label--white">
    <div class="wordmark">
      <div class="wordmark__head">
        <div class="wordmark__name">Colin<br>Fennick</div>
        <span class="wordmark__dot"></span>
      </div>
      <div class="wordmark__meta">EST. 1977 | CLARE VALLEY</div>
      <div class="wordmark__variety">PINOT NOIR ROSE</div>
      <div class="wordmark__vintage">VINTAGE 2018</div>
    </div>
  </section>

  <section class="label label--slate">
    <div class="wordmark">
      <div class="wordmark__head">
        <div class="wordmark__name">Colin<br>Fennick</div>
        <span class="wordmark__dot"></span>
      </div>
      <div class="wordmark__meta">EST. 1977 | CLARE VALLEY</div>
      <div class="wordmark__variety">PINOT NOIR ROSE</div>
      <div class="wordmark__vintage">VINTAGE 2018</div>
    </div>
  </section>

  <section class="label label--slate-bright">
    <div class="wordmark">
      <div class="wordmark__head">
        <div class="wordmark__name">Colin<br>Fennick</div>
        <span class="wordmark__dot"></span>
      </div>
      <div class="wordmark__meta">EST. 1977 | CLARE VALLEY</div>
      <div class="wordmark__variety">PINOT NOIR ROSE</div>
      <div class="wordmark__vintage">VINTAGE 2018</div>
    </div>
  </section>

  <!-- Range lockups -->
  <div class="range range--shiraz">
    <div class="wordmark">
      <div class="wordmark__head">
        <div class="wordmark__name">Colin<br>Fennick</div>
        <span class="wordmark__dot"></span>
      </div>
      <div class="wordmark__meta">EST. 1977 | CLARE VALLEY</div>
      <div class="variety-row">
        <div class="wordmark__variety">SHIRAZ</div>
        <div class="wordmark__vintage">VINTAGE<br>2018</div>
      </div>
    </div>
  </div>

  <div class="range range--shiraz-cab">
    <div class="wordmark">
      <div class="wordmark__head">
        <div class="wordmark__name">Colin<br>Fennick</div>
        <span class="wordmark__dot"></span>
      </div>
      <div class="wordmark__meta">EST. 1977 | CLARE VALLEY</div>
      <div class="wordmark__variety">SHIRAZ CABERNET</div>
      <div class="wordmark__vintage">VINTAGE 2018</div>
    </div>
  </div>

  <div class="range range--riesling">
    <div class="wordmark">
      <div class="wordmark__head">
        <div class="wordmark__name">Colin<br>Fennick</div>
        <span class="wordmark__dot"></span>
      </div>
      <div class="wordmark__meta">EST. 1977 | CLARE VALLEY</div>
      <div class="variety-row">
        <div class="wordmark__variety">RIESLING</div>
        <div class="wordmark__vintage">VINTAGE<br>2018</div>
      </div>
    </div>
  </div>

  <div class="range range--cab-sav">
    <div class="wordmark">
      <div class="wordmark__head">
        <div class="wordmark__name">Colin<br>Fennick</div>
        <span class="wordmark__dot"></span>
      </div>
      <div class="wordmark__meta">EST. 1977 | CLARE VALLEY</div>
      <div class="wordmark__variety">CABERNEY SAUVIGNON</div>
      <div class="wordmark__vintage">VINTAGE 2018</div>
    </div>
  </div>

</body>
</html>
```